Images and design ideas provided: Postcard size flier

2 sided postcard size flier to hand people on the street.

A FUN tax business needs a postcard size flier to hand people on the street. Not a typical serious, quiet, office so make the image fun!

Exact wording, logo and key images provided. You are free to add other images as you see fit (such as money).

Side 1: Use image of lady looking up (she should be looking at text provided).All spanish and english text provided. Logo in bottom right corner. Address at bottom of card.

Side 2: Image of lady holding money and pointing. Remove money and have her holding a sign/or some other creative way to have her looking at text. All spanish and english text provided. Logo in bottom right corner. Address at bottom of card.

Size: 4" x 6" horizontal or vertical is ok
Each side can be different and image/design does not have to be related.

Target Market(s)

Age 18-35

Industry/Entity Type

Accounting

Font styles to use
Sans Serif

Colors

Designer to choose colors to be used in the design.

Requirements
Must have
• Use text document provided. All text goes on both sides.
• Should be easy to read from a few feet away.
Nice to have
• Bright colors to attract attention of people walking by to grab flier/card. Images of money ok.
Should not have
• No images of calculators or typical accounting tax forms.

```html
<!DOCTYPE html>
<html lang="en">
<head>
<meta charset="utf-8">
<title>Bright Refund Co. – Postcard Flier</title>
<link href="https://fonts.googleapis.com/css2?family=Open+Sans:wght@400;600;700&family=Montserrat:wght@600;700;800&display=swap" rel="stylesheet">
<style>
  :root {
    --stage: #e9e9e9;
    --aqua: #2cc7dd;
    --aqua-light: #6fe0ee;
    --aqua-deep: #16b3cc;
    --ink: #2b2b2b;
    --band: #333333;
    --white: #ffffff;
    --paper: #f4f4f4;
    --warm: #e7a98f;
    --warm-red: #e06a5f;
  }
  * { box-sizing: border-box; margin: 0; padding: 0; }
  html, body { width: 1200px; height: 960px; overflow: hidden; }
  body {
    background: var(--stage);
    display: flex; flex-direction: column; align-items: center; justify-content: center;
    gap: 36px;
    font-family: "Open Sans", Arial, sans-serif;
  }
  .postcard {
    position: relative; width: 630px; height: 420px; overflow: hidden;
    box-shadow: 0 6px 18px rgba(0,0,0,.18);
  }

  /* Side one: English */
  .side-english { background: linear-gradient(180deg, var(--aqua) 0%, var(--aqua-light) 55%, var(--aqua) 100%); }
  .side-english .backdrop {
    position: absolute; inset: 0 0 40px 0;
    background: radial-gradient(ellipse at 30% 60%, rgba(255,255,255,.28), transparent 60%);
  }
  .brand-name {
    position: absolute; font-weight: 700; letter-spacing: .5px; color: var(--white);
    display: flex; align-items: center; gap: 10px; white-space: nowrap;
  }
  .brand-name .brand-dot { width: 14px; height: 14px; border-radius: 50%; background: currentColor; }
  .side-english .brand-name { left: 30px; top: 70px; font-size: 26px; }
  .headline-en {
    position: absolute; left: 30px; top: 186px; color: var(--white);
    font-size: 30px; font-weight: 600; line-height: 1.1; white-space: nowrap;
  }
  .headline-en .amount { color: var(--ink); font-weight: 700; }
  .subline-en { position: absolute; left: 32px; top: 228px; color: var(--white); font-size: 16px; font-weight: 600; }
  .call-pill {
    position: absolute; left: 30px; top: 296px; padding: 9px 18px;
    background: var(--white); color: var(--aqua-deep); border-radius: 24px;
    font-size: 16px; font-weight: 600; white-space: nowrap;
  }
  .dollar {
    position: absolute; color: var(--ink); font-weight: 700;
  }
  .dollar.light { color: var(--white); }
  .address-bar {
    position: absolute; left: 0; right: 0; bottom: 0; height: 40px;
    background: var(--band); color: var(--white); font-size: 11px;
    display: flex; align-items: center; padding-left: 26px;
  }
  .photo-money-lady {
    position: absolute; left: 390px; top: 60px; width: 210px; height: 320px;
    background: linear-gradient(180deg, var(--warm) 0%, var(--warm-red) 100%);
  }

  /* Side two: Spanish */
  .side-spanish { background: var(--paper); font-family: "Montserrat", Arial, sans-serif; }
  .side-spanish .top-panel {
    position: absolute; left: 0; top: 0; width: 250px; height: 150px;
    background: var(--aqua); clip-path: polygon(0 0, 100% 0, 70% 100%, 0 100%);
  }
  .side-spanish .brand-name { left: 30px; top: 44px; font-size: 20px; }
  .photo-sign-lady {
    position: absolute; left: 170px; top: 0; right: 0; height: 150px;
    background: linear-gradient(90deg, #f1d9cc 0%, var(--warm) 55%, #f1e4dc 100%);
  }
  .headline-es {
    position: absolute; left: 0; right: 0; top: 178px; text-align: center;
    color: var(--ink); font-size: 30px; font-weight: 800;
  }
  .subline-es {
    position: absolute; left: 0; right: 0; top: 222px; text-align: center;
    color: var(--ink); font-size: 18px; font-weight: 700;
  }
  .call-band {
    position: absolute; left: 0; right: 0; top: 270px; height: 66px;
    background: var(--band); color: var(--white);
    display: flex; align-items: center; justify-content: center;
    font-size: 28px; font-weight: 700; letter-spacing: 1px;
  }
  .address-line {
    position: absolute; left: 0; right: 0; top: 354px; text-align: center;
    color: var(--ink); font-size: 14px; font-weight: 600;
  }
</style>
</head>
<body>

  <section class="postcard side-english">
    <div class="backdrop"></div>
    <div class="brand-name"><span class="brand-dot"></span>Bright Refund Co.</div>
    <p class="headline-en">Get <span class="amount">$100</span> Cash Now!</p>
    <p class="subline-en">with paid tax preparation</p>
    <div class="call-pill">CALL NOW (555) 014-2837</div>
    <div class="photo-money-lady" role="img" aria-label="Photo of a smiling woman in a red t-shirt holding a fan of dollar bills"></div>
    <span class="dollar light" style="left:388px;top:36px;font-size:15px">$</span>
    <span class="dollar" style="left:352px;top:120px;font-size:16px">$</span>
    <span class="dollar" style="left:606px;top:66px;font-size:22px">$</span>
    <span class="dollar light" style="left:340px;top:344px;font-size:15px">$</span>
    <div class="address-bar">418 Harbor Ave. Riverside NY 10021</div>
  </section>

  <section class="postcard side-spanish">
    <div class="photo-sign-lady" role="img" aria-label="Photo of a smiling woman leaning over and pointing down at the text"></div>
    <div class="top-panel"></div>
    <div class="brand-name"><span class="brand-dot"></span>Bright Refund Co.</div>
    <p class="headline-es">Reciba $100 en efectivo ahora!</p>
    <p class="subline-es">con la preparacion pagada de sus impuestos</p>
    <div class="call-band">CALL NOW (555) 014-2837</div>
    <p class="address-line">418 Harbor Ave. Riverside NY 10021</p>
  </section>

</body>
</html>
```